Sleep Consulting Business

Hello I need a business card design with similar colors to my logo that was created. I help mom/parents whose little ones are having sleep issues. Are you able to recreate the picture with the girl sleeping onto a business card using a picture that I provide. That would be one side with my logo on top and on the other side would the following:
My name (in bigger letters than the rest. maybe written in script
title
email
website
phone
instagram
I have included color Inspo
Contact Information for Business Card
Full Name, number, email, website, ig page
Look and feel
Each slider illustrates characteristics of the customer's brand and the style your logo design should communicate.

```html
<!DOCTYPE html>
<html lang="en">
<head>
<meta charset="utf-8">
<title>Hushwood Sleep – Business Card</title>
<link rel="stylesheet" href="https://fonts.googleapis.com/css2?family=Josefin+Sans:wght@400;600&family=Poppins:wght@400&family=Allura&display=swap">
<style>
  :root {
    --stage: #2a2a2a;
    --peach: #cf9780;
    --taupe: #8c817b;
    --night: #1d1816;
    --paper: #ffffff;
  }
  * { margin: 0; padding: 0; box-sizing: border-box; }
  html, body { width: 1200px; height: 689px; overflow: hidden; }
  body { background: var(--stage); position: relative; font-family: "Poppins", sans-serif; }

  .card {
    position: absolute;
    top: 190px;
    width: 540px;
    height: 310px;
    border-radius: 22px;
    overflow: hidden;
  }

  /* Front */
  .card--front { left: 40px; }
  .front-photo {
    position: absolute; inset: 0;
    background: radial-gradient(ellipse at 55% 40%, #4a3a31 0%, #2c231f 45%, var(--night) 100%);
  }
  .front-brand {
    position: absolute; inset: 0;
    display: flex; flex-direction: column; align-items: center; justify-content: center;
  }
  .brand-name {
    display: flex; align-items: center; gap: 12px;
    font-family: "Josefin Sans", sans-serif;
    font-weight: 600;
    color: var(--peach);
    letter-spacing: 0.14em;
    text-transform: uppercase;
    white-space: nowrap;
  }
  .brand-dot { border-radius: 50%; background: var(--taupe); flex: none; }
  .front-brand .brand-name { font-size: 34px; }
  .front-brand .brand-dot { width: 30px; height: 30px; }

  /* Back */
  .card--back { left: 620px; background: var(--paper); }
  .back-wave { position: absolute; inset: 0; }
  .back-brand { position: absolute; left: 30px; top: 118px; }
  .back-brand .brand-name { font-size: 20px; }
  .back-brand .brand-dot { width: 18px; height: 18px; }

  .person { position: absolute; right: 30px; top: 24px; text-align: right; }
  .person-name {
    font-family: "Allura", cursive;
    font-size: 50px;
    line-height: 1;
    color: var(--taupe);
  }
  .person-title {
    font-family: "Josefin Sans", sans-serif;
    font-size: 12px;
    letter-spacing: 0.12em;
    color: var(--peach);
    margin-top: 4px;
    white-space: nowrap;
  }

  .contact { position: absolute; list-style: none; color: var(--paper); font-size: 12.5px; line-height: 1; }
  .contact li { display: flex; align-items: center; gap: 8px; margin-top: 7px; white-space: nowrap; }
  .contact--left { left: 30px; bottom: 20px; }
  .contact--right { right: 30px; bottom: 82px; }
  .contact--right li { justify-content: flex-end; }
  .contact-icon {
    width: 18px; height: 18px; border: 1.2px solid var(--paper); border-radius: 50%;
    display: flex; align-items: center; justify-content: center; flex: none;
    font-size: 10px; line-height: 1;
  }
  .contact-icon svg { width: 10px; height: 10px; }
</style>
</head>
<body>

  <section class="card card--front">
    <div class="front-photo" role="img" aria-label="Dim photo of a little girl sleeping peacefully under a duvet"></div>
    <div class="front-brand">
      <div class="brand-name"><span class="brand-dot"></span>Hushwood Sleep</div>
    </div>
  </section>

  <section class="card card--back">
    <svg class="back-wave" viewBox="0 0 540 310" preserveAspectRatio="none" aria-hidden="true">
      <path d="M0,262 C80,215 140,235 210,195 S330,150 400,150 S500,150 540,125 L540,310 L0,310 Z" fill="var(--peach)"/>
      <path d="M0,254 C80,207 140,227 210,187 S330,142 400,142 S500,142 540,117" fill="none" stroke="var(--peach)" stroke-width="2"/>
      <path d="M0,266 C80,219 140,239 210,199 S330,154 400,154 S500,154 540,129" fill="none" stroke="var(--paper)" stroke-width="2.5"/>
    </svg>

    <div class="person">
      <div class="person-name">Maren Ellery</div>
      <div class="person-title">MANAGING DIRECTOR</div>
    </div>

    <div class="back-brand">
      <div class="brand-name"><span class="brand-dot"></span>Hushwood Sleep</div>
    </div>

    <ul class="contact contact--left">
      <li>
        <span class="contact-icon"><svg viewBox="0 0 10 10"><path d="M2,1 L4,1 L4.5,3 L3.4,3.8 C4,5 5,6 6.2,6.6 L7,5.5 L9,6 L9,8 C5,8.5 1.5,5 2,1 Z" fill="var(--paper)"/></svg></span>
        044-555 018 234
      </li>
      <li>
        <span class="contact-icon"><svg viewBox="0 0 10 10"><rect x="1" y="2.5" width="8" height="5.5" fill="none" stroke="var(--paper)" stroke-width="1"/><path d="M1,2.5 L5,5.5 L9,2.5" fill="none" stroke="var(--paper)" stroke-width="1"/></svg></span>
        hello@hushwoodsleep.com
      </li>
    </ul>

    <ul class="contact contact--right">
      <li>www.hushwoodsleep.com
        <span class="contact-icon"><svg viewBox="0 0 10 10"><circle cx="5" cy="5" r="3.8" fill="none" stroke="var(--paper)" stroke-width="0.9"/><ellipse cx="5" cy="5" rx="1.6" ry="3.8" fill="none" stroke="var(--paper)" stroke-width="0.9"/><line x1="1.2" y1="5" x2="8.8" y2="5" stroke="var(--paper)" stroke-width="0.9"/></svg></span>
      </li>
      <li>instagram.hushwoodsleep
        <span class="contact-icon">@</span>
      </li>
    </ul>
  </section>

</body>
</html>
```